RM Halvora businesscard project

RM Halvora Ltd is a freshly founded small (3 employees), young (average age is 30 years) company, living from the road transportation market without own tools.
We would like to have an impressive, new-line, cool busines card for a freshly founded forwarding company on an overcrowded market which raises attention and makes the potential partners eager to work with us.

Target Market(s)

The main profile of the company is logistic/forwarding on road.

Industry/Entity Type

Freight Forwarding

Contact Information for Business Card

Name: Berki Zsófia
Title: general manager
mobile nr: +36-70/482-5193
fax nr: +36-1/534-9061
e-mail: zsofia.berki@rmhalvora.example
info@rmhalvora.example
website address: http://www.rmhalvora.example
and if possible maybe some funny or helpful info on the back

Requirements
Must have
• contact details above
Nice to have
• some really nice and catching back-side (info, graphics, useful tool info... anything)
Should not have
• trucks, road, ship, airplane on it...

```html
<!DOCTYPE html>
<html lang="hu">
<head>
<meta charset="utf-8">
<title>RM Halvora – Business Card</title>
<link rel="stylesheet" href="https://fonts.googleapis.com/css2?family=Open+Sans:wght@400;700&display=swap">
<style>
  :root {
    --bg-top: #e9e9e9;
    --bg-bottom: #fafafa;
    --panel-light: #ffffff;
    --panel-edge: #ededed;
    --brand-blue: #5a84b9;
    --banner-text: #f3f5f8;
    --ink: #444444;
    --brand-ink: #3b3836;
  }
  * { margin: 0; padding: 0; box-sizing: border-box; }
  html, body {
    width: 1200px;
    height: 800px;
    overflow: hidden;
  }
  body {
    font-family: "Open Sans", "Segoe UI", sans-serif;
  }
  .card {
    position: relative;
    width: 1200px;
    height: 800px;
    overflow: hidden;
    background: linear-gradient(180deg, var(--bg-top) 0%, var(--bg-bottom) 100%);
  }
  .brand-panel {
    position: absolute;
    left: 0;
    top: 0;
    width: 440px;
    height: 800px;
  }
  .brand {
    position: absolute;
    left: 37px;
    top: 290px;
    width: 300px;
    text-align: center;
  }
  .brand-mark {
    display: block;
    width: 90px;
    height: 90px;
    margin: 0 auto 72px;
    background: var(--brand-blue);
  }
  .brand-name {
    font-size: 46px;
    font-weight: 400;
    line-height: 60px;
    color: var(--brand-ink);
    letter-spacing: -0.5px;
    white-space: nowrap;
  }
  .name-banner {
    position: absolute;
    left: 448px;
    top: 146px;
    width: 770px;
    height: 125px;
    border-radius: 8px;
    background: var(--brand-blue);
    color: var(--banner-text);
    text-align: center;
    padding-right: 18px;
  }
  .person-name {
    font-size: 44px;
    font-weight: 700;
    line-height: 1;
    padding-top: 18px;
  }
  .person-title {
    font-size: 30px;
    font-weight: 400;
    line-height: 1;
    padding-top: 10px;
  }
  .contact {
    position: absolute;
    left: 460px;
    top: 412px;
    width: 740px;
    text-align: center;
    color: var(--ink);
    font-size: 31px;
    line-height: 41.5px;
    list-style: none;
  }
</style>
</head>
<body>
  <main class="card">
    <svg class="brand-panel" viewBox="0 0 440 800" aria-hidden="true">
      <defs>
        <linearGradient id="panelFill" x1="0" y1="0" x2="0" y2="1">
          <stop offset="0" stop-color="#ededed"/>
          <stop offset="0.45" stop-color="#ffffff"/>
          <stop offset="1" stop-color="#ededed"/>
        </linearGradient>
        <filter id="panelShadow" x="-20%" y="-20%" width="140%" height="140%">
          <feDropShadow dx="2" dy="0" stdDeviation="4" flood-color="#000" flood-opacity="0.12"/>
        </filter>
      </defs>
      <ellipse cx="0" cy="400" rx="412" ry="515" fill="url(#panelFill)" filter="url(#panelShadow)"/>
    </svg>

    <div class="brand">
      <span class="brand-mark"></span>
      <div class="brand-name">RM Halvora</div>
    </div>

    <header class="name-banner">
      <h1 class="person-name">Berki Zsófia</h1>
      <p class="person-title">General Manager</p>
    </header>

    <ul class="contact">
      <li>Mobile No : +36-70/482-5193</li>
      <li>Fax No : +36-1/534-9061</li>
      <li>e-mail : zsofia.berki@rmhalvora.example</li>
      <li>info@rmhalvora.example</li>
      <li>Website : http://www.rmhalvora.example</li>
    </ul>
  </main>
</body>
</html>
```